Asphalt Paving Specialists Business Cards

Our company is TREVIN ASPHALT. We need a business cards two of our asphalt paving team members. We're asphalt specialists.
I need two made up please. The details on the front of the each business card i would like please is as follows.
Address is 87 Marrowby St, Kellmore, WA, 6284.

Company Director
Gordon Pelliway
gord@trevinpave.com.au
04 58 736 042
www.trevinpave.com.au

Supervisor
Curtis Vonnegard
curtis@trevinpave.com.au
0462 873 105
www.trevinpave.com.au

We do all aspects of Asphalt Paving. Specific Services include - Driveways, Carparks & sub-divisions. All Roads. Repairs and Maintenance.

We provide free quotes!

I dont have a certain way i want them to look so im open to all designs :)

** I have uploaded our logo for the TREVIN ASPHALT. HOWEVER, CAN YOU PLEASE GET RID OF THE ( PTY LTD )

Thank you
Renata Fulch
TREVIN ASPHALT

Target Market(s)

Home owners and Business Owners

Contact Information for Business Card

Asphalt Paving Specialists. All aspects of Asphalt. Residential, Commercial & Industrial. Based in Brisbane.

Font styles to use
Sans Serif

Colors

Designer to choose colors to be used in the design.

Requirements
Nice to have
• maybe an image of a driveway? or Asphalt?

```html
<!DOCTYPE html>
<html lang="en">
<head>
<meta charset="utf-8">
<title>TREVIN ASPHALT — Business Cards</title>
<link rel="stylesheet" href="https://fonts.googleapis.com/css2?family=Open+Sans:wght@400;600;700&display=swap">
<style>
  :root {
    --bg: #2a2a2a;
    --card-white: #ffffff;
    --brand-blue: #00a9e0;
    --ink: #222222;
    --ink-soft: #333333;
    --swoosh: #111111;
  }
  * { margin: 0; padding: 0; box-sizing: border-box; }
  html, body { width: 1200px; height: 900px; overflow: hidden; }
  body {
    background: var(--bg);
    font-family: "Open Sans", Arial, sans-serif;
    position: relative;
  }
  .card {
    position: absolute;
    width: 640px;
    height: 366px;
    border-radius: 30px;
    overflow: hidden;
    box-shadow: 0 18px 40px rgba(0,0,0,0.45);
  }
  /* Front */
  .card-front { left: 90px; top: 70px; background: var(--card-white); }
  .card-front .wave { position: absolute; inset: 0; }
  .brand {
    position: absolute; right: 40px; top: 46px;
    display: flex; align-items: center; gap: 10px;
    font-weight: 700; font-size: 28px; letter-spacing: 1px;
    color: var(--ink);
  }
  .brand-dot { width: 18px; height: 18px; border-radius: 50%; background: var(--brand-blue); }
  .contact { position: absolute; left: 48px; top: 92px; color: var(--ink-soft); }
  .person-name { font-weight: 700; font-size: 21px; color: var(--brand-blue); line-height: 1.2; }
  .person-role { font-size: 17px; color: var(--ink); margin-bottom: 14px; }
  .address { font-size: 15.5px; line-height: 1.35; margin-bottom: 12px; }
  .contact-list { list-style: none; font-size: 15.5px; line-height: 1.55; }
  .contact-list li { display: flex; align-items: center; gap: 10px; }
  .contact-list svg { width: 13px; height: 13px; flex: none; }

  /* Back */
  .card-back {
    left: 470px; top: 460px; background: var(--brand-blue);
    color: #ffffff; text-align: center;
    display: flex; flex-direction: column; align-items: center; justify-content: center;
  }
  .services-title {
    font-weight: 600; font-size: 19px; letter-spacing: 0.5px;
    padding-bottom: 6px; border-bottom: 1.5px solid #ffffff; margin-bottom: 46px;
  }
  .services-list { list-style: none; font-weight: 600; font-size: 19px; letter-spacing: 0.5px; line-height: 1.5; }
</style>
</head>
<body>

<section class="card card-front" aria-label="Business card front">
  <svg class="wave" viewBox="0 0 640 366" aria-hidden="true">
    <path d="M0,330 C170,352 340,330 440,250 C500,200 565,150 640,144 L640,366 L0,366 Z" fill="var(--brand-blue)"/>
    <path d="M0,314 C170,342 340,318 440,238 C500,186 565,136 640,130 L640,144 C565,150 500,200 440,250 C340,330 170,352 0,330 Z" fill="var(--swoosh)"/>
  </svg>

  <div class="brand">
    <span class="brand-dot"></span>
    <span class="brand-name">TREVIN ASPHALT</span>
  </div>

  <div class="contact">
    <p class="person-name">Gordon Pelliway</p>
    <p class="person-role">Company Director</p>
    <p class="address">87 Marrowby St<br>Kellmore, WA, 6284</p>
    <ul class="contact-list">
      <li>
        <svg viewBox="0 0 16 16"><circle cx="8" cy="8" r="7" fill="none" stroke="var(--brand-blue)" stroke-width="1.6"/><path d="M6 4.5 L7.5 6.5 L6.8 7.5 C7.3 8.6 8 9.3 9 9.8 L10 9 L11.8 10.5 L10.8 11.8 C8 11.5 5 8.5 4.8 5.6 Z" fill="var(--brand-blue)"/></svg>
        04 58 736 042
      </li>
      <li>
        <svg viewBox="0 0 16 16"><rect x="1" y="3" width="14" height="10" rx="1" fill="var(--brand-blue)"/><path d="M1.5 3.5 L8 9 L14.5 3.5" fill="none" stroke="#fff" stroke-width="1.4"/></svg>
        gord@trevinpave.com.au
      </li>
      <li>
        <svg viewBox="0 0 16 16"><circle cx="8" cy="8" r="7" fill="none" stroke="var(--brand-blue)" stroke-width="1.4"/><ellipse cx="8" cy="8" rx="3" ry="7" fill="none" stroke="var(--brand-blue)" stroke-width="1.2"/><path d="M1 8 H15 M2.5 4.5 H13.5 M2.5 11.5 H13.5" stroke="var(--brand-blue)" stroke-width="1.1"/></svg>
        www.trevinpave.com.au
      </li>
    </ul>
  </div>
</section>

<section class="card card-back" aria-label="Business card back">
  <h2 class="services-title">OUR SERVICES</h2>
  <ul class="services-list">
    <li>• DRIVEWAYS • CARPARKS &amp; SUB-DIVISIONS</li>
    <li>• ALL ROADS • REPAIRS &amp; MAINTENANCE.</li>
  </ul>
</section>

</body>
</html>
```